Kestrel Study Hub - CQV Exam Prep

We are starting a CQV exam prep training company with later focus on project management classes.
We need a Wordpress website designed with the following general requirements:
1) English and Thai language pages
2) 5 pages to start (Home Page, About us (Testimonials), Contact us, About CQV Exam, Book a class (events page).
3) Turn over all design files so that we can host on HostWren, etc
4) Bi-lingual English/Thai
5) Plugins for Live Assistance / Monitoring (English goes to one contact number....Thai will go go another number)
6) Plugins for Shopping Cart, Add to Cart Button, Payment Systems/Methods
7) Plugins Social Media Links, Social Sharing Button
Online Chat Box
8) Trustmarks (/Security Signs)
9) Special Offers
10) Social media links (Chatterly, Bleeper, CareerWEB)
11) Zintro Admarks plugin
12) Plugin for mobile phone display
13) Images sliders with high-quality images
14) Coinvey API integration connected to class booking system.

```html
<!DOCTYPE html>
<html lang="en">
<head>
<meta charset="utf-8">
<title>Kestrel Study Hub – CQV Exam Prep</title>
<link href="https://fonts.googleapis.com/css2?family=Roboto:wght@300;400;500;700&family=Oswald:wght@400;500&display=swap" rel="stylesheet">
<style>
:root{
  --orange:#f7960f;
  --orange-dark:#e4620f;
  --ink:#2b2b2b;
  --text:#555;
  --muted:#8a8a8a;
  --line:#e2e2e2;
  --soft:#f6f5f5;
  --grey-band:#e9ebeb;
  --footer:#232323;
  --white:#fff;
}
*{box-sizing:border-box;margin:0;padding:0}
html,body{width:1200px;height:2715px;overflow:hidden}
body{font-family:"Roboto",Arial,sans-serif;color:var(--text);background:var(--white)}
.page{position:relative;width:1200px;height:2715px;overflow:hidden}
.abs{position:absolute}

/* top bar */
.topbar{left:0;top:0;width:1200px;height:108px;background:var(--orange)}
.brand{left:100px;top:30px;color:var(--white);font-size:26px;font-weight:700;letter-spacing:.5px}
.topmeta{right:100px;top:14px;display:flex;align-items:center;gap:16px;font-size:11px;color:var(--white)}
.paybadge{background:var(--white);color:#1d4f91;font-weight:700;font-size:11px;padding:3px 7px;border-radius:2px}
.live{left:940px;top:50px;width:160px;height:42px;background:var(--orange-dark);border-radius:4px;color:var(--white);font-size:12px;font-weight:700;display:flex;align-items:center;gap:10px;padding-left:8px}
.live .dot{width:28px;height:28px;border-radius:50%;background:#f15a24;border:2px solid rgba(255,255,255,.6)}

/* nav */
.nav{left:0;top:108px;width:1200px;height:78px;background:var(--white)}
.nav a{position:absolute;top:30px;font-size:12px;font-weight:500;color:var(--ink);text-decoration:none}
.nav a.active{color:var(--orange)}
.search{left:856px;top:16px;width:244px;height:46px;border:1px solid #ddd;border-radius:3px;font-size:11px;color:#aaa;padding:16px 12px}
.search svg{position:absolute;right:12px;top:13px}

/* hero */
.hero{left:0;top:186px;width:1200px;height:621px;background:linear-gradient(180deg,#6b5a4c 0%,#9b8470 45%,#b49a82 100%)}
.hero-title{left:0;top:430px;width:1200px;text-align:center;font-family:"Oswald",sans-serif;font-size:33px;font-weight:400;color:var(--white);letter-spacing:.3px}
.hero-sub{left:0;top:480px;width:1200px;text-align:center;font-size:12px;font-weight:500;color:var(--white);line-height:22px;text-transform:uppercase}
.hero-arrows{left:565px;top:548px;display:flex;gap:14px}

/* welcome */
.welcome{left:0;top:807px;width:1200px;height:503px;background:var(--soft)}
.sec-title{width:1200px;left:0;text-align:center;font-size:24px;color:var(--ink);font-weight:400}
.rule{height:1px;background:var(--orange)}
.intro{left:220px;width:760px;text-align:center;font-size:11px;line-height:20px;color:var(--muted)}
.feature{width:238px;height:262px;top:183px;background:var(--white);border:1px solid #ddd;box-shadow:0 1px 3px rgba(0,0,0,.08);text-align:center}
.feature .ic{position:absolute;left:83px;top:16px;width:72px;height:72px;border-radius:50%;border:1.5px solid #555;display:flex;align-items:center;justify-content:center}
.feature h3{position:absolute;top:103px;width:100%;font-size:15px;font-weight:400;color:var(--ink)}
.feature .ul{position:absolute;left:64px;top:133px;width:110px;height:1px;background:var(--orange)}
.feature p{position:absolute;top:150px;left:18px;right:18px;font-size:11px;line-height:19px;color:var(--text)}
.feature .more{position:absolute;left:107px;top:222px}

/* coaching */
.coach-img{width:322px;height:192px;top:1430px;border:1px solid #ddd;background:var(--white);padding:12px}
.coach-img div{width:100%;height:100%}
.coach h3{position:absolute;width:322px;text-align:center;font-size:20px;font-weight:400;color:var(--ink);top:1642px}
.coach p{position:absolute;width:322px;text-align:center;font-size:11px;line-height:20px;top:1683px;padding:0 14px}
.cart-btn{position:absolute;width:104px;height:36px;top:1762px;border:1px solid #999;border-radius:4px;color:var(--orange);font-size:11px;font-weight:700;text-align:center;line-height:34px}

/* about + testimonial */
.band{left:0;top:1845px;width:1200px;height:405px;background:var(--grey-band)}
.about-box{left:100px;top:1900px;width:654px;height:292px;background:var(--white);box-shadow:0 1px 4px rgba(0,0,0,.12)}
.about-box h2{position:absolute;left:24px;top:26px;font-size:17px;font-weight:500;color:var(--ink)}
.about-img{position:absolute;left:22px;top:72px;width:264px;height:185px;background:linear-gradient(160deg,#4a5a3a,#1e1e22 60%,#7e8f5a)}
.about-lead{position:absolute;left:312px;top:72px;width:318px;font-size:11px;line-height:19px;font-weight:700;color:var(--ink)}
.about-body{position:absolute;left:312px;top:115px;width:318px;font-size:11px;line-height:19px;color:var(--muted)}
.testi-head{left:848px;top:1916px;font-size:17px;font-weight:500;color:var(--ink)}
.testi-body{left:782px;top:1962px;width:318px;font-size:11px;line-height:19px;color:var(--text);text-align:justify;text-indent:56px}
.testi-name{right:100px;top:2150px;font-size:15px;font-weight:500;color:var(--ink)}

/* signup */
.signup-title{left:100px;top:2288px;font-size:24px;color:var(--ink);font-weight:400}
.field{top:2338px;width:268px;height:47px;border:1px solid #ccc;font-size:11px;color:#999;padding:17px 10px;background:var(--white)}
.submit{left:993px;top:2338px;width:107px;height:47px;background:var(--orange);color:var(--white);font-size:12px;font-weight:700;text-align:center;line-height:47px}

/* footer */
.footer{left:0;top:2430px;width:1200px;height:285px;background:var(--footer);color:#cfcfcf}
.footer h4{position:absolute;top:33px;font-size:17px;font-weight:500;color:var(--white)}
.footer ul{position:absolute;top:72px;list-style:none;font-size:11px;line-height:20px}
.footer ul.arrows li::before{content:"\25B8  ";color:#aaa}
.trust{left:633px;top:172px;width:102px;height:44px;background:var(--white);border:1px solid #999}
.trust span{position:absolute;left:8px;top:10px;width:22px;height:22px;background:#c8102e}
.social{position:absolute;top:158px;width:42px;height:42px;border-radius:50%;background:#a0700c;color:var(--white);font-size:8px;font-weight:500;display:flex;align-items:center;justify-content:center}
.copy{left:100px;top:242px;font-size:11px;color:#999}
</style>
</head>
<body>
<div class="page">

  <header class="abs topbar">
    <div class="abs brand">Kestrel Study Hub</div>
    <div class="abs topmeta">
      <span>Lingual</span>
      <span>English &#9662;</span>
      <svg width="16" height="14" viewBox="0 0 16 14"><path d="M1 1h3l2 8h8l1-6H5" fill="none" stroke="#fff" stroke-width="1.6"/><circle cx="7" cy="12" r="1.3" fill="#fff"/><circle cx="13" cy="12" r="1.3" fill="#fff"/></svg>
      <span class="paybadge">Coinvey</span>
    </div>
    <div class="abs live"><span class="dot"></span>LIVE ASSISTANCE</div>
  </header>

  <nav class="abs nav">
    <a class="active" style="left:98px">HOME</a>
    <a style="left:186px">ABOUT US</a>
    <a style="left:298px">TESTIMONIALS</a>
    <a style="left:440px">CONTACT US</a>
    <a style="left:567px">ABOUT CQV EXAM</a>
    <a style="left:729px">BOOK A CLASS</a>
    <div class="abs search">Search...
      <svg width="18" height="18" viewBox="0 0 18 18"><circle cx="7.5" cy="7.5" r="5.5" fill="none" stroke="#333" stroke-width="2"/><path d="M11.5 11.5l5 5" stroke="#333" stroke-width="2.4"/></svg>
    </div>
  </nav>

  <section class="abs hero" role="img" aria-label="Photo of smiling students in a classroom, one raising a hand">
    <h1 class="abs hero-title">CQV EXAM PREP TRAINING COMPANY</h1>
    <p class="abs hero-sub">Denouncing pleasure and praising pain was born and I will give you a complete account<br>of the system, and expound the actual teachings of the great explorer</p>
    <div class="abs hero-arrows">
      <svg width="28" height="28" viewBox="0 0 28 28"><circle cx="14" cy="14" r="12.5" fill="none" stroke="#fff" stroke-width="1.6"/><path d="M19 14H9m4-4-4 4 4 4" fill="none" stroke="#fff" stroke-width="1.8"/></svg>
      <svg width="28" height="28" viewBox="0 0 28 28"><circle cx="14" cy="14" r="12.5" fill="none" stroke="#fff" stroke-width="1.6"/><path d="M9 14h10m-4-4 4 4-4 4" fill="none" stroke="#fff" stroke-width="1.8"/></svg>
    </div>
  </section>

  <section class="abs welcome">
    <h2 class="abs sec-title" style="top:56px">Welcome to Kestrel Study Hub</h2>
    <div class="abs rule" style="left:350px;top:96px;width:500px"></div>
    <p class="abs intro" style="top:114px">Eiusmod tempor incididunt ut labore et dolore magna aliqua. Ut enim ad minim veniam, quis nostrud exercitation ullamco laboris nisi ut aliquip commodo consequat. Duis aute irure dolor in reprehenderit in voluptate velit esse cillum dolore eu fugiat nulla pariatur.</p>

    <div class="abs feature" style="left:100px">
      <div class="ic"><svg width="36" height="36" viewBox="0 0 36 36"><circle cx="18" cy="11" r="6" fill="var(--orange)"/><path d="M6 32c0-8 5-12 12-12s12 4 12 12z" fill="var(--orange)"/></svg></div>
      <h3>HOW WE CAN HELP YOU?</h3><div class="ul"></div>
      <p>Fieldnote integrates types of investigative information such as addresses, vehicles, subjects.</p>
      <svg class="more" width="24" height="24" viewBox="0 0 24 24"><circle cx="12" cy="12" r="10" fill="none" stroke="#aaa"/><path d="M8 9l4 4 4-4M8 13l4 4 4-4" fill="none" stroke="var(--orange)" stroke-width="1.6"/></svg>
    </div>
    <div class="abs feature" style="left:354px">
      <div class="ic"><svg width="36" height="36" viewBox="0 0 36 36"><rect x="5" y="7" width="24" height="17" rx="1.5" fill="none" stroke="var(--orange)" stroke-width="3"/><path d="M13 30h8M17 24v6" stroke="var(--orange)" stroke-width="3"/><circle cx="28" cy="10" r="5" fill="var(--orange)"/></svg></div>
      <h3>ONLINE COACHING?</h3><div class="ul"></div>
      <p>Fieldnote integrates types of investigative information such as addresses, vehicles, subjects.</p>
      <svg class="more" width="24" height="24" viewBox="0 0 24 24"><circle cx="12" cy="12" r="10" fill="none" stroke="#aaa"/><path d="M8 9l4 4 4-4M8 13l4 4 4-4" fill="none" stroke="var(--orange)" stroke-width="1.6"/></svg>
    </div>
    <div class="abs feature" style="left:608px">
      <div class="ic"><svg width="36" height="36" viewBox="0 0 36 36"><path d="M18 3l4.6 9.6 10.4 1.3-7.6 7.2 2 10.4L18 26.4 8.6 31.5l2-10.4L3 13.9l10.4-1.3z" fill="var(--orange)"/></svg></div>
      <h3>BEST COACHES</h3><div class="ul"></div>
      <p>Fieldnote integrates types of investigative information such as addresses, vehicles, subjects.</p>
      <svg class="more" width="24" height="24" viewBox="0 0 24 24"><circle cx="12" cy="12" r="10" fill="none" stroke="#aaa"/><path d="M8 9l4 4 4-4M8 13l4 4 4-4" fill="none" stroke="var(--orange)" stroke-width="1.6"/></svg>
    </div>
    <div class="abs feature" style="left:862px">
      <div class="ic"><svg width="36" height="36" viewBox="0 0 36 36"><rect x="12" y="5" width="20" height="15" fill="none" stroke="var(--orange)" stroke-width="2.6"/><circle cx="8" cy="14" r="4" fill="var(--orange)"/><path d="M3 32v-8c0-3 2-5 5-5s5 2 5 5v8z" fill="var(--orange)"/><path d="M22 20v10M17 32l5-4 5 4" stroke="var(--orange)" stroke-width="2.4" fill="none"/></svg></div>
      <h3>CQV COACHING</h3><div class="ul"></div>
      <p>Fieldnote integrates types of investigative information such as addresses, vehicles, subjects.</p>
      <svg class="more" width="24" height="24" viewBox="0 0 24 24"><circle cx="12" cy="12" r="10" fill="none" stroke="#aaa"/><path d="M8 9l4 4 4-4M8 13l4 4 4-4" fill="none" stroke="var(--orange)" stroke-width="1.6"/></svg>
    </div>
  </section>

  <section class="coach">
    <h2 class="abs sec-title" style="top:1342px">What Can CQV Coaching Do For You?</h2>
    <div class="abs rule" style="left:316px;top:1393px;width:569px"></div>

    <div class="abs coach-img" style="left:100px"><div role="img" aria-label="Photo of a teacher helping a student at a chalkboard" style="background:linear-gradient(135deg,#2f3a3a,#6d7a78 55%,#c9c3b6)"></div></div>
    <h3 style="left:100px">NUMQUAM EIUS MODI</h3>
    <p style="left:100px">There are many variations of passages of Lorem Ipsum available, but the majority have suffered alteration in some form injected humour, or randomised.</p>
    <div class="cart-btn" style="left:209px">ADD TO CART</div>

    <div class="abs coach-img" style="left:440px"><div role="img" aria-label="Photo of students working on a laptop together" style="background:linear-gradient(135deg,#7a4a32,#d8b6a0 50%,#efe7e0)"></div></div>
    <h3 style="left:440px">TEMPORA INCIDUNT</h3>
    <p style="left:440px">There are many variations of passages of Lorem Ipsum available, but the majority have suffered alteration in some form injected humour, or randomised.</p>
    <div class="cart-btn" style="left:549px">ADD TO CART</div>

    <div class="abs coach-img" style="left:778px"><div role="img" aria-label="Photo of two students studying at a library table" style="background:linear-gradient(135deg,#6a4a2c,#b98f5c 50%,#d9c3a5)"></div></div>
    <h3 style="left:778px">PRAESENTIUM</h3>
    <p style="left:778px">There are many variations of passages of Lorem Ipsum available, but the majority have suffered alteration in some form injected humour, or randomised.</p>
    <div class="cart-btn" style="left:887px">ADD TO CART</div>
  </section>

  <section class="abs band"></section>
  <article class="abs about-box">
    <h2>About Our Kestrel Study Hub</h2>
    <div class="about-img" role="img" aria-label="Photo of a smiling graduate in cap and gown"></div>
    <p class="about-lead">There are many variations of passages of Lorem Ipsum available, but the majority have suffered.</p>
    <p class="about-body">Alteration in some form, by injected humour, or randomised words which don't look even slightly believable. If you are going to use a passage of the Lorem Ipsum, you need to be sure there isn't anything embarrassing hidden in the middle of text. All the Lorem Ipsum generators on the Internet tend to repeat predefined chunks as necessary, making this the first true generator on the Internet.</p>
  </article>

  <svg class="abs" style="left:780px;top:1908px" width="54" height="44" viewBox="0 0 54 44"><path d="M2 44V24C2 10 9 2 22 0v8c-7 2-10 7-10 14h10v22zM30 44V24C30 10 37 2 50 0v8c-7 2-10 7-10 14h10v22z" fill="#cfd2d2"/></svg>
  <h3 class="abs testi-head">Testimonal</h3>
  <p class="abs testi-body">There are many variations of passages of Lorem Ipsum available, but the majority have suffered alteration in some form, by injected humour, or randomised words which don't look even slightly believable. If you are going to use a passage of Lorem Ipsum, you the need to be sure there isn't anything embarrassing hidden in the middle of text. All the Lorem Ipsum generators on the Internet tend to repeat pre-defined chunks as necessary.</p>
  <svg class="abs" style="left:782px;top:2150px" width="38" height="18" viewBox="0 0 38 18"><rect width="18" height="18" fill="#111"/><rect x="20" width="18" height="18" fill="#111"/><path d="M11 4l-5 5 5 5M27 4l5 5-5 5" fill="none" stroke="#fff" stroke-width="2"/></svg>
  <div class="abs testi-name">-- Avery Lin</div>

  <h2 class="abs signup-title">SIGN UP TO GET&nbsp; DEALS?</h2>
  <div class="abs field" style="left:100px">Your Email :*</div>
  <div class="abs field" style="left:400px">Your Password :*</div>
  <div class="abs field" style="left:696px">Phonenumber :*</div>
  <div class="abs submit">SUBMIT</div>

  <footer class="abs footer">
    <h4 style="left:100px">About Us</h4>
    <ul style="left:100px"><li>Home</li><li>About us</li><li>Testimonials</li><li>Contact us</li><li>About CQV Exam</li><li>Book a class</li></ul>
    <h4 style="left:302px">Recent News</h4>
    <ul style="left:302px;width:240px"><li>08-12-2015: USD-CNY cross rate still has lot of room to move</li><li>08-09-2015: Copper has a very bearish weekly formation</li><li>07-22-2015: A Potential Corn Trade</li></ul>
    <h4 style="left:633px">Our Classes</h4>
    <ul class="arrows" style="left:633px"><li>Classic Sightseeing Tour</li><li>Pirate Treasure Hunt</li><li>Agent Falcon Tour</li><li>D Day Duck</li></ul>
    <div class="abs trust"><span></span></div>
    <h4 style="left:889px">Contact Us</h4>
    <ul style="left:889px"><li>Lorem Ipsum 1555 Harbor Lane #200</li><li>Marlow Bay, CA 95008 1-312-555-0147</li><li>contact@kestrelstudyhub.com</li></ul>
    <div class="social" style="left:880px">Chatterly</div>
    <div class="social" style="left:936px">Bleeper</div>
    <div class="social" style="left:992px">Plusly</div>
    <div class="social" style="left:1048px"><svg width="16" height="16" viewBox="0 0 16 16"><circle cx="3" cy="13" r="2" fill="#fff"/><path d="M1 7a8 8 0 0 1 8 8M1 2a13 13 0 0 1 13 13" fill="none" stroke="#fff" stroke-width="2.2"/></svg></div>
    <div class="abs copy">Copyright © 2016 Kestrel Study Hub.com&nbsp; - All Rights Reserved</div>
  </footer>

</div>
</body>
</html>
```